Summit Reach Marketing
"Lifting your Brand Plans Past Every Limit"
Summit Reach Marketing - Marketing
Creative Brief
Use same font as used in my logo
Berlin
Professional
Nadia Kfoury
Marketing Consultant
Summit Reach Marketing T 961 1 847063 F 961 1 847063 M 961 3 402815 Po.Box: 738419 Beirut W http://www.summitreachmkt.me E nadiak@summitreachmkt.me E sales@summitreachmkt.me E info@summitreachmkt.me UAE | LEBANON | Summit Reach Marketing ... Lifting your Brand Plans Past Every Limit
nadia@summitreachmkt.me
on the back of the business card i want it to be in a form that ables someone to write additional notes. I maybe suggest it to be done in a form of a postcard. I suggest you check out www.summitreachmkt.me to see the spirit of the company and colors

```html
<!DOCTYPE html>
<html lang="en">
<head>
<meta charset="utf-8">
<title>Summit Reach Marketing – Stationery</title>
<link rel="stylesheet" href="https://fonts.googleapis.com/css2?family=Open+Sans:wght@400;600;700&display=swap">
<style>
  :root{
    --brand-red:#a31f2e;
    --brand-red-dark:#7e1522;
    --brand-pink:#e6b3b9;
    --paper:#ffffff;
    --ink:#4a4a4a;
    --muted:#8a8a8a;
    --rule:#d9d9d9;
    --field:#ececec;
    --backdrop:#e9e7e4;
  }
  *{box-sizing:border-box;margin:0;padding:0}
  html,body{width:1200px;height:915px;overflow:hidden}
  body{background:var(--backdrop);font-family:"Open Sans",Arial,sans-serif;color:var(--ink);position:relative}

  .sheet{position:absolute;background:var(--paper);box-shadow:0 2px 6px rgba(0,0,0,.18);overflow:hidden}
  .swoosh{position:absolute;inset:0;width:100%;height:100%}
  .red{fill:var(--brand-red)}
  .pink{fill:var(--brand-pink)}

  .brand{display:flex;align-items:center;gap:6px;position:relative}
  .brand-dot{width:22px;height:22px;border-radius:50%;background:var(--brand-red);flex:none}
  .brand-name{font-weight:700;font-size:10px;color:var(--brand-red);letter-spacing:.3px;text-transform:uppercase;white-space:nowrap}
  .tagline{font-size:6px;color:var(--muted)}

  .contact{position:absolute;font-size:5.5px;line-height:1.55;color:var(--ink);white-space:nowrap}

  /* business card front */
  .card-front{left:40px;top:50px;width:220px;height:128px}
  .card-front .brand{position:absolute;left:16px;top:14px;flex-direction:column;align-items:center;gap:4px}
  .card-front .brand-dot{width:24px;height:24px}
  .card-front .brand-name{font-size:7px;line-height:1.2;text-align:center}
  .card-front .person{position:absolute;left:112px;top:14px}
  .person-name{font-size:9px;font-weight:700;color:var(--brand-red);white-space:nowrap}
  .person-role{font-size:5.5px;color:var(--muted);white-space:nowrap}
  .card-front .contact{left:112px;top:40px}

  /* business card back */
  .card-back{left:280px;top:50px;width:220px;height:128px;background:var(--brand-red);display:flex;flex-direction:column;align-items:center;justify-content:center;gap:6px}
  .card-back .brand-dot{background:#fff}
  .card-back .brand-name{color:#fff}
  .card-back .tagline{color:#f4d9dc}
  .note-lines{width:150px;border-top:1px solid rgba(255,255,255,.45);margin-top:6px}

  /* envelopes */
  .env-flap{left:40px;top:205px;width:460px;height:190px}
  .env-flap .brand{position:absolute;left:50%;top:118px;transform:translateX(-50%)}
  .env-dl{width:460px;height:215px}
  .env-dl.one{left:40px;top:420px}
  .env-dl.two{left:40px;top:660px}
  .env-dl .brand{position:absolute;left:20px;top:22px}
  .env-dl .contact{left:150px;top:60px}

  /* letterhead + fax */
  .letterhead,.fax{width:305px;height:405px}
  .top{top:35px}.bottom{top:475px}
  .lh-a{left:525px}.fax-a{left:855px}
  .letterhead .brand,.fax .brand{position:absolute;left:22px;top:22px}
  .letterhead .contact,.fax .contact{left:150px;top:325px}
  .fax-title{position:absolute;right:22px;top:26px;font-weight:700;font-size:14px;color:var(--brand-red)}
  .fax-fields{position:absolute;left:22px;right:22px;top:70px;display:grid;grid-template-columns:36px 1fr 36px 1fr;gap:3px}
  .fax-fields span{font-size:6px;height:14px;line-height:14px;padding-left:3px}
  .fax-fields .label{background:var(--field);color:var(--muted)}
  .fax-fields .value{border-bottom:1px solid var(--rule)}
  .fax-checks{position:absolute;left:22px;right:22px;top:148px;display:flex;justify-content:space-between;font-size:5.5px;color:var(--muted)}
  .fax-checks span::before{content:"";display:inline-block;width:5px;height:5px;border:1px solid var(--muted);margin-right:2px;vertical-align:-1px}
  .fax-rule{position:absolute;left:22px;right:22px;top:162px;border-top:1px solid var(--rule)}
</style>
</head>
<body>

<section class="sheet card-front">
  <svg class="swoosh" viewBox="0 0 220 128" preserveAspectRatio="none" aria-hidden="true">
    <path class="pink" d="M0 96 C60 110 140 112 220 92 V128 H0Z"/>
    <path class="red" d="M0 106 C70 120 150 120 220 102 V128 H0Z"/>
  </svg>
  <div class="brand"><span class="brand-dot"></span><span class="brand-name">Summit Reach<br>Marketing</span></div>
  <div class="person"><div class="person-name">Nadia Kfoury</div><div class="person-role">Marketing Consultant</div></div>
  <div class="contact">T 961 1 847063<br>M 961 3 402815<br>Po.Box: 738419 Beirut<br>nadiak@summitreachmkt.me<br>www.summitreachmkt.me</div>
</section>

<section class="sheet card-back">
  <div class="brand"><span class="brand-dot"></span><span class="brand-name">Summit Reach Marketing</span></div>
  <div class="tagline">"Lifting your Brand Plans Past Every Limit"</div>
  <div class="note-lines"></div>
</section>

<section class="sheet env-flap">
  <svg class="swoosh" viewBox="0 0 460 190" preserveAspectRatio="none" aria-hidden="true">
    <path d="M0 0 L230 150 L460 0" fill="none" stroke="#cfcfcf" stroke-width="1"/>
    <path d="M0 190 L190 95 M460 190 L270 95" fill="none" stroke="#e0e0e0" stroke-width="1"/>
  </svg>
  <div class="brand"><span class="brand-dot"></span><span class="brand-name">Summit Reach Marketing</span></div>
</section>

<section class="sheet env-dl one">
  <svg class="swoosh" viewBox="0 0 460 215" preserveAspectRatio="none" aria-hidden="true">
    <path class="pink" d="M460 40 C390 100 330 170 290 215 H310 C350 170 400 110 460 70Z"/>
    <path class="red" d="M460 70 C400 110 350 170 310 215 H460Z"/>
  </svg>
  <div class="brand"><span class="brand-dot"></span><span class="brand-name">Summit Reach Marketing</span></div>
  <div class="contact">Summit Reach Marketing<br>T 961 1 847063 | M 961 3 402815<br>Po.Box: 738419 Beirut<br>W http://www.summitreachmkt.me<br>E info@summitreachmkt.me</div>
</section>
<section class="sheet env-dl two">
  <svg class="swoosh" viewBox="0 0 460 215" preserveAspectRatio="none" aria-hidden="true">
    <path class="pink" d="M460 40 C390 100 330 170 290 215 H310 C350 170 400 110 460 70Z"/>
    <path class="red" d="M460 70 C400 110 350 170 310 215 H460Z"/>
  </svg>
  <div class="brand"><span class="brand-dot"></span><span class="brand-name">Summit Reach Marketing</span></div>
  <div class="contact">Summit Reach Marketing<br>T 961 1 847063 | M 961 3 402815<br>Po.Box: 738419 Beirut<br>W http://www.summitreachmkt.me<br>E sales@summitreachmkt.me</div>
</section>

<section class="sheet letterhead top lh-a">
  <svg class="swoosh" viewBox="0 0 300 400" preserveAspectRatio="none" aria-hidden="true">
    <path class="pink" d="M215 0 C255 6 285 22 300 48 V36 C285 16 262 4 238 0Z"/>
    <path class="red" d="M238 0 H300 V36 C285 16 262 4 238 0Z"/>
    <path class="pink" d="M0 245 C18 310 60 365 120 400 H104 C52 368 16 320 0 268Z"/>
    <path class="red" d="M0 268 C16 320 52 368 104 400 H0Z"/>
  </svg>
  <div class="brand"><span class="brand-dot"></span><span class="brand-name">Summit Reach Marketing</span></div>
  <div class="contact">Summit Reach Marketing<br>T 961 1 847063 | F 961 1 847063<br>M 961 3 402815 | Po.Box: 738419 Beirut<br>W http://www.summitreachmkt.me<br>E info@summitreachmkt.me</div>
</section>
<section class="sheet letterhead bottom lh-a">
  <svg class="swoosh" viewBox="0 0 300 400" preserveAspectRatio="none" aria-hidden="true">
    <path class="pink" d="M215 0 C255 6 285 22 300 48 V36 C285 16 262 4 238 0Z"/>
    <path class="red" d="M238 0 H300 V36 C285 16 262 4 238 0Z"/>
    <path class="pink" d="M0 245 C18 310 60 365 120 400 H104 C52 368 16 320 0 268Z"/>
    <path class="red" d="M0 268 C16 320 52 368 104 400 H0Z"/>
  </svg>
  <div class="brand"><span class="brand-dot"></span><span class="brand-name">Summit Reach Marketing</span></div>
  <div class="contact">Summit Reach Marketing<br>T 961 1 847063 | F 961 1 847063<br>M 961 3 402815 | Po.Box: 738419 Beirut<br>W http://www.summitreachmkt.me<br>E nadia@summitreachmkt.me</div>
</section>

<section class="sheet fax top fax-a">
  <svg class="swoosh" viewBox="0 0 300 400" preserveAspectRatio="none" aria-hidden="true">
    <path class="pink" d="M0 245 C18 310 60 365 120 400 H104 C52 368 16 320 0 268Z"/>
    <path class="red" d="M0 268 C16 320 52 368 104 400 H0Z"/>
    <path class="red" d="M292 0 H300 V400 H292Z"/>
  </svg>
  <div class="brand"><span class="brand-dot"></span><span class="brand-name">Summit Reach Marketing</span></div>
  <div class="fax-title">FAX</div>
  <div class="fax-fields">
    <span class="label">To</span><span class="value"></span><span class="label">From</span><span class="value"></span>
    <span class="label">Fax</span><span class="value"></span><span class="label">Pages</span><span class="value"></span>
    <span class="label">Phone</span><span class="value"></span><span class="label">Date</span><span class="value"></span>
    <span class="label">Re</span><span class="value"></span><span class="label">CC</span><span class="value"></span>
  </div>
  <div class="fax-checks"><span>Urgent</span><span>For Review</span><span>Please Comment</span><span>Please Reply</span><span>Please Recycle</span></div>
  <div class="fax-rule"></div>
  <div class="contact">Summit Reach Marketing<br>T 961 1 847063 | F 961 1 847063<br>M 961 3 402815 | Po.Box: 738419 Beirut<br>W http://www.summitreachmkt.me<br>E info@summitreachmkt.me</div>
</section>
<section class="sheet fax bottom fax-a">
  <svg class="swoosh" viewBox="0 0 300 400" preserveAspectRatio="none" aria-hidden="true">
    <path class="pink" d="M0 245 C18 310 60 365 120 400 H104 C52 368 16 320 0 268Z"/>
    <path class="red" d="M0 268 C16 320 52 368 104 400 H0Z"/>
    <path class="red" d="M292 0 H300 V400 H292Z"/>
  </svg>
  <div class="brand"><span class="brand-dot"></span><span class="brand-name">Summit Reach Marketing</span></div>
  <div class="fax-title">FAX</div>
  <div class="fax-fields">
    <span class="label">To</span><span class="value"></span><span class="label">From</span><span class="value"></span>
    <span class="label">Fax</span><span class="value"></span><span class="label">Pages</span><span class="value"></span>
    <span class="label">Phone</span><span class="value"></span><span class="label">Date</span><span class="value"></span>
    <span class="label">Re</span><span class="value"></span><span class="label">CC</span><span class="value"></span>
  </div>
  <div class="fax-checks"><span>Urgent</span><span>For Review</span><span>Please Comment</span><span>Please Reply</span><span>Please Recycle</span></div>
  <div class="fax-rule"></div>
  <div class="contact">Summit Reach Marketing<br>T 961 1 847063 | F 961 1 847063<br>M 961 3 402815 | Po.Box: 738419 Beirut<br>W http://www.summitreachmkt.me<br>E sales@summitreachmkt.me</div>
</section>

</body>
</html>
```